Interior decorating services

I would like to have a business card created for my interior decorating business.

Target Market(s)

any one wishing to have their space decorated

Industry/Entity Type

Business

Contact Information for Business Card

Clara J. Whitcombe ; 417-582-6094; quobavent42@pelmora.com

Font styles to use
Serif

Colors

Designer to choose colors to be used in the design.

Requirements
Must have
• nice colors that flow well, and the name of my business: BrivLa Designs
Nice to have
• round logo looking design in the corner

```html
<!DOCTYPE html>
<html lang="en">
<head>
<meta charset="utf-8">
<title>BrivLa Designs — Business Card</title>
<link rel="stylesheet" href="https://fonts.googleapis.com/css2?family=Tinos:wght@400;700&display=swap">
<style>
  :root {
    --backdrop: #1c1c1c;
    --card-teal: #5ca8a7;
    --ink-white: #ffffff;
    --ornament-tint: #b4dad9;
  }
  html, body {
    margin: 0;
    padding: 0;
    width: 1200px;
    height: 902px;
    overflow: hidden;
    background: var(--backdrop);
  }
  .canvas {
    position: relative;
    width: 1200px;
    height: 902px;
  }
  .business-card {
    position: absolute;
    left: 100px;
    top: 165px;
    width: 1000px;
    height: 571px;
    background: var(--card-teal);
    border-radius: 24px;
    font-family: "Tinos", "Times New Roman", serif;
    color: var(--ink-white);
  }
  .frame-line {
    position: absolute;
    left: 47px;
    right: 47px;
    top: 45px;
    bottom: 45px;
    border: 2.5px solid var(--ink-white);
  }
  .corner-ornament {
    position: absolute;
    width: 140px;
    height: 140px;
    background: var(--ornament-tint);
    border-radius: 6px;
  }
  .corner-ornament.top-left { left: 40px; top: 38px; }
  .corner-ornament.top-right { right: 40px; top: 38px; }
  .corner-ornament.bottom-left { left: 40px; bottom: 38px; }
  .corner-ornament.bottom-right { right: 40px; bottom: 38px; }
  .flourish-band {
    position: absolute;
    left: 295px;
    width: 410px;
    height: 64px;
    background: linear-gradient(90deg, rgba(180,218,217,0) 0%, var(--ornament-tint) 25%, var(--ornament-tint) 75%, rgba(180,218,217,0) 100%);
    border-radius: 32px;
  }
  .flourish-band.above-title { top: 88px; }
  .flourish-band.below-title { top: 222px; }
  .business-name {
    position: absolute;
    left: 0;
    right: 0;
    top: 174px;
    margin: 0;
    text-align: center;
    font-size: 38px;
    font-weight: 400;
    letter-spacing: 2px;
    line-height: 1;
  }
  .contact-block {
    position: absolute;
    left: 0;
    right: 0;
    top: 350px;
    text-align: center;
  }
  .person-name {
    margin: 0 0 18px;
    font-size: 41px;
    font-weight: 400;
    line-height: 1;
  }
  .contact-line {
    margin: 0 0 9px;
    font-size: 25px;
    line-height: 1.1;
  }
  .contact-label { font-weight: 700; }
</style>
</head>
<body>
<main class="canvas">
  <section class="business-card">
    <div class="frame-line"></div>

    <div class="corner-ornament top-left" role="img" aria-label="Decorative scrollwork corner ornament"></div>
    <div class="corner-ornament top-right" role="img" aria-label="Decorative scrollwork corner ornament"></div>
    <div class="corner-ornament bottom-left" role="img" aria-label="Decorative scrollwork corner ornament"></div>
    <div class="corner-ornament bottom-right" role="img" aria-label="Decorative scrollwork corner ornament"></div>

    <div class="flourish-band above-title" role="img" aria-label="Symmetric swirl flourish divider"></div>
    <h1 class="business-name">BRIVLA DESIGNS</h1>
    <div class="flourish-band below-title" role="img" aria-label="Symmetric swirl flourish divider"></div>

    <div class="contact-block">
      <p class="person-name">Clara J. Whitcombe</p>
      <p class="contact-line"><span class="contact-label">P:</span> 417-582-6094</p>
      <p class="contact-line"><span class="contact-label">E:</span> quobavent42@pelmora.com</p>
    </div>
  </section>
</main>
</body>
</html>
```